Halvorn Building Inc Business Card Design

We want a business card that stands out; we build high end commercial interiors so card should be professional yet creative and have an architectural/design feel , very clean lines

We have 6 employees so we must be able to change the name, cell and email on each person's card
For the proof Dale Pomfrey is the president
Office Number is (561) 482-3155, Cell ( 561 ) 823-4170

4700 Kestrel Lane Suite 215, Palm Beach Gardens, FL 33403
www.halvornbuild.example
CGC 047395 ( This license must legally be on card)

Target Market(s)

Asset Specialists , Developers, Building owners, architects, business owners

Industry/Entity Type

Construction Company

Contact Information for Business Card

We want a very high end clean look, must incorporate existing logo

Font styles to use
Other font styles liked:
• Gotham, trade gothic, Mrs. Eaves,modern 20, trim or designers' choice

Colors

Designer to choose colors to be used in the design.

Requirements
Must have
• Name, address, CGC 047395, www.halvornbuild.example
• 4700 Kestrel Lane Suite 215, Palm Beach Gardens, FL 33403
• each persons name, cell phone and individual email address ie dalep@halvornbuild.example

```html
<!DOCTYPE html>
<html lang="en">
<head>
<meta charset="utf-8">
<title>Halvorn Building Inc – Business Card</title>
<link rel="stylesheet" href="https://fonts.googleapis.com/css2?family=Montserrat:wght@500;600;700;800&display=swap">
<style>
  :root {
    --backdrop: #808080;
    --paper: #ffffff;
    --navy: #2a2a6e;
    --ink: #0d0d0d;
    --green: #7ac143;
  }
  html, body {
    margin: 0;
    padding: 0;
    width: 1200px;
    height: 1000px;
    overflow: hidden;
    background: var(--backdrop);
    font-family: "Montserrat", Arial, sans-serif;
  }
  .canvas {
    position: relative;
    width: 1200px;
    height: 1000px;
  }
  .card {
    position: absolute;
    left: 257px;
    width: 686px;
    background: var(--paper);
    overflow: hidden;
  }
  .card--front { top: 95px; height: 392px; }
  .card--back { top: 512px; height: 393px; }

  .arc-band {
    position: absolute;
    left: 0;
    top: 0;
    width: 686px;
    height: 392px;
  }

  .brand {
    position: absolute;
    display: flex;
    align-items: center;
    gap: 8px;
    color: var(--navy);
    font-weight: 800;
    line-height: 1;
  }
  .brand__dot {
    width: 12px;
    height: 12px;
    border-radius: 50%;
    background: var(--green);
    flex: none;
  }
  .brand__name {
    display: flex;
    flex-direction: column;
    text-transform: uppercase;
  }
  .brand__main { font-size: 34px; letter-spacing: 0.5px; }
  .brand__sub { font-size: 12px; letter-spacing: 5.2px; margin-top: 4px; }

  .card--front .brand { left: 18px; top: 40px; }
  .card--back .brand { left: 50%; top: 108px; transform: translateX(-50%); }

  .person {
    position: absolute;
    left: 458px;
    top: 175px;
  }
  .person__name {
    margin: 0;
    font-size: 20px;
    font-weight: 700;
    line-height: 1;
    color: var(--ink);
    letter-spacing: 0.3px;
  }
  .person__first { color: var(--navy); }
  .person__title {
    margin: 2px 0 0;
    font-size: 10px;
    font-weight: 700;
    color: var(--ink);
  }

  .contact {
    position: absolute;
    left: 458px;
    top: 316px;
    margin: 0;
    padding: 0;
    list-style: none;
    font-size: 13.5px;
    font-weight: 500;
    line-height: 17px;
    color: var(--ink);
  }

  .address {
    position: absolute;
    left: 0;
    right: 0;
    top: 228px;
    text-align: center;
    color: var(--navy);
    font-style: normal;
    font-weight: 600;
    font-size: 12.5px;
    line-height: 15px;
  }
  .address__license {
    display: block;
    font-size: 14.5px;
    font-weight: 500;
    margin-top: 2px;
  }

  .web-bar {
    position: absolute;
    left: 0;
    bottom: 0;
    width: 100%;
    height: 39px;
    background: var(--ink);
    border-top: 3px solid var(--green);
    box-shadow: 0 -1px 0 var(--paper);
    color: var(--paper);
    font-weight: 700;
    font-size: 15px;
    letter-spacing: 12.4px;
    line-height: 36px;
    padding-left: 26px;
    box-sizing: border-box;
    white-space: nowrap;
  }
</style>
</head>
<body>
<main class="canvas">

  <section class="card card--front" aria-label="Card front">
    <svg class="arc-band" viewBox="0 0 686 392" aria-hidden="true">
      <path d="M371 0 C300 120 300 280 373 392 L398 392 C318 280 318 120 396 0 Z" fill="var(--ink)"/>
      <path d="M396 0 C318 120 318 280 398 392 L421 392 C342 280 342 120 421 0 Z" fill="var(--green)"/>
    </svg>

    <div class="brand">
      <span class="brand__dot"></span>
      <span class="brand__name">
        <span class="brand__main">Halvorn</span>
        <span class="brand__sub">Building</span>
      </span>
    </div>

    <div class="person">
      <h1 class="person__name"><span class="person__first">DALE</span> POMFREY</h1>
      <p class="person__title">PRESIDENT</p>
    </div>

    <ul class="contact">
      <li>OFFICE: (561) 482-3155</li>
      <li>CELL: (561) 823-4170</li>
      <li>dalep@halvornbuild.example</li>
    </ul>
  </section>

  <section class="card card--back" aria-label="Card back">
    <div class="brand">
      <span class="brand__dot"></span>
      <span class="brand__name">
        <span class="brand__main">Halvorn</span>
        <span class="brand__sub">Building</span>
      </span>
    </div>

    <address class="address">
      4700 Kestrel Lane Suite 215<br>
      Palm Beach Gardens, FL 33403
      <span class="address__license">CGC 047395</span>
    </address>

    <div class="web-bar">www.halvornbuild.example</div>
  </section>

</main>
</body>
</html>
```